Packaging Design New Cosmetics Range

Small Establish online Beauty company is expanding it's product range into Serums, Sprays and Creams . We are looking for a new fresh packaging design for this launch.
We only use products that are Organic , Not Tested on Animals and Natural products
We would be interested in viewing a White Design , Black design and a designer choice of colors .
First Products are
Rose Water in 100ml glass bottle with box
and a set of 3 Face Serums Vit C , Retinol and Hyaluronic in 30ml Glass bottle = Box
Scrubs and creams will launch later in Q1 2020 however would like a similar feel across all products
Target Market(s)
SEA / US Markets
Industry/Entity Type
Cosmetics
Colors
Designer to choose colors to be used in the design.
Requirements
Must have
- Space Allocated for Product Use and Bar Codes on Box
Nice to have
- Organic , Not tested on animal Logo's

```html
<!DOCTYPE html>
<html lang="en">
<head>
<meta charset="utf-8">
<title>Olemya Rose Water – Packaging</title>
<link rel="stylesheet" href="https://fonts.googleapis.com/css2?family=Lato:wght@300;400;700&display=swap">
<style>
  :root {
    --rose: #d987a3;
    --rose-soft: #e39ab2;
    --rose-tint: #f3d5df;
    --white: #ffffff;
    --white-tint: #ecb3c6;
    --backdrop: #f2eced;
    --label-line: #ecd3dc;
  }
  * { box-sizing: border-box; margin: 0; padding: 0; }
  html, body { width: 1200px; height: 1000px; overflow: hidden; }
  body {
    background: var(--backdrop);
    font-family: "Lato", Arial, sans-serif;
    position: relative;
  }

  /* Box panels */
  .box-panel {
    position: absolute;
    top: 120px;
    width: 300px;
    height: 760px;
    background: var(--rose);
    color: var(--white);
  }
  .box-back { left: 40px; }
  .box-front { left: 860px; }

  .back-details {
    position: absolute;
    left: 0; right: 0; bottom: 70px;
    text-align: center;
    font-size: 12px;
    line-height: 1.35;
    font-weight: 400;
  }
  .back-details strong { font-weight: 700; }
  .back-web { margin-top: 12px; font-size: 16px; font-weight: 700; }

  .pattern-area { position: absolute; display: block; }
  .box-front .pattern-area { left: 30px; top: 30px; width: 90px; height: 105px; background: var(--white-tint); }

  .product-name {
    position: absolute;
    font-weight: 300;
    line-height: 1.12;
  }
  .box-front .product-name { left: 30px; top: 205px; font-size: 31px; }

  .claim-badges { position: absolute; display: flex; flex-direction: column; gap: 20px; }
  .box-front .claim-badges { left: 34px; top: 330px; }
  .claim-badge { width: 44px; height: 44px; border-radius: 50%; display: block; }
  .box-front .claim-badge { background: var(--white); }

  .brand-name {
    position: absolute;
    writing-mode: vertical-rl;
    font-weight: 300;
    letter-spacing: 2px;
    line-height: 1;
    white-space: nowrap;
  }
  .box-front .brand-name { right: 24px; top: 130px; font-size: 104px; color: var(--white); }

  .volume { position: absolute; left: 30px; bottom: 70px; font-size: 17px; font-weight: 400; }

  /* Bottle label */
  .bottle-label {
    position: absolute;
    left: 400px; top: 120px;
    width: 400px; height: 560px;
    background: var(--white);
    color: var(--rose);
    border: 1px solid var(--label-line);
  }
  .bottle-label .pattern-area { left: 40px; top: 50px; width: 100px; height: 110px; background: var(--rose-tint); }
  .bottle-label .product-name { left: 40px; top: 190px; font-size: 32px; }
  .bottle-label .claim-badges { left: 42px; top: 330px; }
  .bottle-label .claim-badge { background: var(--rose); }
  .bottle-label .brand-name { right: 50px; top: 90px; font-size: 112px; color: var(--rose); }

  /* Round cap label */
  .round-label {
    position: absolute;
    left: 460px; top: 700px;
    width: 280px; height: 280px;
    border-radius: 50%;
    background: var(--white);
    border: 1px solid var(--label-line);
    color: var(--rose-soft);
    overflow: hidden;
  }
  .round-copy {
    position: absolute;
    right: 78px; top: 24px;
    width: 170px;
    text-align: right;
    font-size: 8.5px;
    line-height: 1.3;
  }
  .round-copy h3 { font-size: 9px; font-weight: 700; margin-top: 4px; }
  .round-copy strong { font-weight: 700; }
  .round-copy p { margin-bottom: 3px; }
  .round-web { font-size: 12px; font-weight: 700; margin-top: 6px; }
  .round-label .brand-name { right: 26px; top: 36px; font-size: 44px; color: var(--rose); }
</style>
</head>
<body>

  <section class="box-panel box-back" aria-label="Box back panel">
    <div class="back-details">
      <p>Produced by <strong>Olemya Beauty</strong></p>
      <p>27 Soi Orchid, Kathu</p>
      <p>Phuket 83150 | Hotline: 611357802</p>
      <p class="back-web">olemya.th</p>
    </div>
  </section>

  <section class="bottle-label" aria-label="Bottle label">
    <div class="pattern-area" role="img" aria-label="Decorative pattern area"></div>
    <h2 class="product-name">Rose<br>Water</h2>
    <div class="claim-badges">
      <span class="claim-badge" role="img" aria-label="Organic badge"></span>
      <span class="claim-badge" role="img" aria-label="Not tested on animals badge"></span>
    </div>
    <p class="brand-name">olemya</p>
  </section>

  <section class="round-label" aria-label="Round information label">
    <div class="round-copy">
      <h3>SUGGESTED USE</h3>
      <p>With eyes and mouth closed, mist directly onto face and neck. Use morning, afternoon and night, before or after makeup. Use as needed to give skin a dewy finish.</p>
      <h3>INGREDIENTS</h3>
      <p>100% natural Rosewater</p>
      <p><strong>Olemya means "Gentle Light"</strong><br>Cruelty-free means neither ingredient nor product have been tested on animals.</p>
      <p>Produced by <strong>Olemya Beauty</strong><br>27 Soi Orchid, Kathu, Phuket<br>Customer Hotline: 611357802</p>
      <p class="round-web">olemya.th</p>
    </div>
    <p class="brand-name">olemya</p>
  </section>

  <section class="box-panel box-front" aria-label="Box front panel">
    <div class="pattern-area" role="img" aria-label="Decorative pattern area"></div>
    <h2 class="product-name">Rose<br>Water</h2>
    <div class="claim-badges">
      <span class="claim-badge" role="img" aria-label="Organic badge"></span>
      <span class="claim-badge" role="img" aria-label="Not tested on animals badge"></span>
    </div>
    <p class="brand-name">olemya</p>
    <p class="volume">100ml</p>
  </section>

</body>
</html>
```